We are looking for a simple design that would be uplifting for
upscale drug addicts

MERIDIAN CIRCLE

PLEASE SEE THE LINK FOR TAG LINE AND CONTENT

thank you.

here is all the actual info we need and we want something like this...

http://assets.qlm.brivostore.com/rest/items/7c2910e5b337de81f94a02bd57e644163ab9fe0a6712?uid=bd31c9e2f7a04c18b6e0d44721fa93c5%2fdrafts&expires=1408211537&signature=kTp4WmQxNvLzHa8YbEoRcJsGf2B%3d

The shape and colors don't have to be like what I posted it is only an example.

Target Market(s)

Wall Street, internet and creative types, men, early 30's,
upwardly mobile, drug addicts

current site

bkltornavel.com

now launching new name Meridian Circle

Industry/Entity Type

Drug

Requirements
Must have
• upscale look, great font
Should not have
• a corporate look but should not look like a clinic.

```html
<!DOCTYPE html>
<html lang="en">
<head>
<meta charset="UTF-8">
<title>Meridian Circle – Business Card</title>
<link href="https://fonts.googleapis.com/css2?family=Source+Sans+3:wght@400&display=swap" rel="stylesheet">
<style>
  :root {
    --card-blue: #0070bb;
    --accent-violet: #3d3a8c;
    --ink-white: #ffffff;
    --ink-dark: #111111;
    --card-edge: #b5b5b5;
    --page: #ffffff;
  }
  * { margin: 0; padding: 0; box-sizing: border-box; }
  html, body {
    width: 1200px;
    height: 758px;
    overflow: hidden;
    background: var(--page);
    font-family: "Source Sans 3", "Myriad Pro", sans-serif;
  }
  .business-card {
    position: absolute;
    left: 46px;
    top: 49px;
    width: 1113px;
    height: 660px;
    border: 1px solid var(--card-edge);
    overflow: hidden;
    background: var(--ink-white);
  }
  .brand-field {
    position: absolute;
    left: 0;
    top: 0;
    width: 100%;
    height: 577px;
    background: var(--card-blue);
    overflow: hidden;
  }
  .brand-glow {
    position: absolute;
    left: -40px;
    top: -150px;
    width: 540px;
    height: 540px;
    border-radius: 50%;
    background: radial-gradient(circle at 50% 50%, rgba(61, 58, 140, 0) 55%, rgba(61, 58, 140, 0.45) 85%, rgba(61, 58, 140, 0) 100%);
  }
  .brand-block {
    position: absolute;
    left: 8px;
    top: 110px;
    width: 440px;
    text-align: center;
    color: var(--ink-white);
  }
  .brand-name {
    font-size: 40px;
    font-weight: 400;
    letter-spacing: 0.3px;
    line-height: 1.1;
  }
  .brand-tagline {
    margin-top: 6px;
    font-size: 23px;
    line-height: 1.2;
  }
  .contact-block {
    position: absolute;
    left: 627px;
    top: 186px;
    width: 500px;
    text-align: center;
    color: var(--ink-white);
  }
  .contact-name {
    font-size: 40px;
    line-height: 1.05;
    letter-spacing: 0.3px;
  }
  .contact-role {
    font-size: 29px;
    line-height: 1.15;
  }
  .contact-address {
    margin-top: 56px;
    font-size: 30px;
    line-height: 1.15;
    font-style: normal;
  }
  .contact-phones {
    margin-top: 42px;
    font-size: 30px;
    line-height: 1.15;
  }
  .email-band {
    position: absolute;
    left: 0;
    top: 577px;
    width: 100%;
    height: 83px;
    display: flex;
    align-items: center;
    justify-content: center;
    font-size: 31px;
    color: var(--ink-dark);
  }
</style>
</head>
<body>
  <div class="business-card">
    <div class="brand-field">
      <div class="brand-glow" role="img" aria-label="Soft violet decorative accent behind the brand name"></div>
      <div class="brand-block">
        <h1 class="brand-name">MERIDIAN CIRCLE</h1>
        <p class="brand-tagline">We don’t cut any corners when it<br>comes to your longterm recovery</p>
      </div>
      <div class="contact-block">
        <p class="contact-name">DANIEL VARRO, CASAC</p>
        <p class="contact-role">Program Coordinator</p>
        <address class="contact-address">418 W. 63rd St. Suite 307<br>NEW YORK, NY 10023</address>
        <p class="contact-phones">212 .555 .0147<br>212 .555 .0148</p>
      </div>
    </div>
    <div class="email-band">counselor@halstonwellnyc.com</div>
  </div>
</body>
</html>
```